Tidewalk Intro Course QM Dive Bonaire

QM Dive is looking for a great flyer to promote our Tidewalk Intro Course around Bonaire, the Caribbean.

Bonaire is shore dive capital of the world.
Our guests rent a pick-up truck. we would like to inform them about the possibilities of the Tidewalk Intro Dive.

We have the logo, images and text available. Its the catchy and mind blowing design we are looking for to create an eye-catch flyer.
One side will be in English, the other side will be in Dutch.

Target Market(s)

Visitors (non divers) of the island Bonaire

Industry/Entity Type

Diving industry

Font styles to use
Sans Serif

Colors
0094D4
00A9DD
6FCCEA
C7EBF8
E9F6FB
F0912C
F2A743
F7CA91
FBE8D2
FDF5EE

Requirements
Must have
• The picture with the car and divers next to it is mandatory. Inspire to go for a tidewalk intro dive, show the beauty under water, easy to come dive with us, just takes half a day
Should not have
• Should not have pictures taken not around Bonaire.

```html
<!DOCTYPE html>
<html lang="en">
<head>
<meta charset="utf-8">
<title>Tidewalk Intro Course on Bonaire – QM Dive</title>
<link rel="stylesheet" href="https://fonts.googleapis.com/css2?family=Open+Sans:wght@400;700;800&display=swap">
<style>
  :root {
    --deep-blue: #0094D4;
    --sea-blue: #00A9DD;
    --lagoon: #6FCCEA;
    --foam: #C7EBF8;
    --mist: #E9F6FB;
    --orange: #F0912C;
    --sand-light: #FDF5EE;
    --sand: #FBE8D2;
    --ink: #1b1b1b;
  }
  * { margin: 0; padding: 0; box-sizing: border-box; }
  html, body { width: 849px; height: 1200px; overflow: hidden; background: #fff; }
  .flyer {
    position: relative;
    width: 849px;
    height: 1200px;
    overflow: hidden;
    font-family: "Open Sans", Arial, sans-serif;
    color: var(--ink);
  }
  .reef-photo {
    position: absolute;
    left: 0; top: 0;
    width: 849px; height: 430px;
    background:
      radial-gradient(ellipse 320px 140px at 260px 300px, rgba(140,170,120,0.55), transparent 70%),
      radial-gradient(ellipse 300px 160px at 700px 320px, rgba(150,110,120,0.45), transparent 70%),
      linear-gradient(180deg, #2f6fb4 0%, #3f8cc4 40%, #5a9fae 75%, #7fb7b0 100%);
  }
  .beach-photo {
    position: absolute;
    left: 0; top: 400px;
    width: 849px; height: 800px;
    background:
      linear-gradient(180deg,
        rgba(255,255,255,0) 0%,
        #2ec4cf 4%,
        #18b7c9 10%,
        #5fd3d6 16%,
        #bfeae6 22%,
        #f4f1ea 30%,
        #f7efe3 55%,
        #efe2cf 100%);
  }
  .brand {
    position: absolute;
    top: 40px; left: 0;
    width: 849px;
    text-align: center;
    font-weight: 800;
    font-size: 52px;
    letter-spacing: 1px;
    color: var(--orange);
  }
  .content {
    position: absolute;
    left: 20px; top: 513px;
    width: 810px;
  }
  h1, h2 {
    font-weight: 700;
    font-size: 25px;
    line-height: 32px;
  }
  p, li {
    font-weight: 700;
    font-size: 17px;
    line-height: 26px;
  }
  .intro { margin-top: 6px; }
  .perks { margin-top: 26px; }
  .perks ul { list-style: none; margin-top: 4px; }
  .perks li::before { content: "• "; }
  .paradise { margin-top: 44px; }
  .paradise p { margin-top: 6px; }
  .call-to-action {
    margin-top: 26px;
    font-size: 21px;
    line-height: 30px;
    width: 680px;
  }
  .partner-badge {
    position: absolute;
    left: 760px; top: 1072px;
    width: 72px; height: 72px;
    border-radius: 50%;
    background: var(--deep-blue);
  }
</style>
</head>
<body>
<div class="flyer">
  <div class="reef-photo" role="img" aria-label="Underwater reef scene with a sea turtle swimming above corals and sea fans"></div>
  <div class="beach-photo" role="img" aria-label="Turquoise Caribbean shallows meeting a light sandy beach"></div>

  <div class="brand">QM Dive</div>

  <main class="content">
    <section>
      <h1>Tidewalk Intro Course on Bonaire</h1>
      <p class="intro">Fall in love with diving in our underwater paradise. Under the guidance of a dive instructor you will learn the basic skills for peaceful diving in a fun and easy way.</p>
    </section>

    <section class="perks">
      <h2>Develop a passion for marine life</h2>
      <ul>
        <li>Ages 10 and up can sign up for our tidewalk intro dive</li>
        <li>You'll dive straight into the water after a brief theoretic introduction</li>
        <li>The Tidewalk Intro Course will take 3-4 hours</li>
        <li>Before participating, you are required to fill out a medical questionnaire</li>
        <li>A group consists of a maximum of 4 people</li>
        <li>Experience the splendor of the ocean without much distraction by other divers</li>
        <li>And enjoy a lot of personal attention given by your instructor</li>
      </ul>
    </section>

    <section class="paradise">
      <h2>Underwater paradise</h2>
      <p>Bonaire is the place to learn how to scuba dive. After a brief introduction we will directly dive into the sea, where the reef starts in shallow waters. We know the perfect dive sites for beginners. Here, the sea bed slopes gradually down and you'll be amazed by the most beautiful fish and corals.</p>
    </section>

    <p class="call-to-action">Stop by at our Front office and we are happy to answer all your questions or to book your 'Tidewalk Intro Dive'!</p>
  </main>

  <div class="partner-badge" aria-hidden="true"></div>
</div>
</body>
</html>
```